Real Estate "For Sale" Sign for construction company

We need a sign that we can use to hang on a post and place on the road when we sell a property. The sign will be simple and will need to mainly feature our logo (files attached), as well as the words "For Sale", and then our phone number "(555) 617 3489". The sign will hang on a post that'll look something like the attached picture.

Target Market(s)

Home buyers

Industry/Entity Type

Real Estate

Font styles to use
Serif
Sans Serif

Colors
0054AA
0677BA
7BADD7
CADEEF
E8F1F8
0094D4
00A9DD
6FCCEA
C7EBF8
E9F6FB

Requirements
Must have
• For Sale & our phone number

```html
<!DOCTYPE html>
<html lang="en">
<head>
<meta charset="utf-8">
<title>For Sale Sign</title>
<link rel="stylesheet" href="https://fonts.googleapis.com/css2?family=Roboto:wght@300;500;700;900&display=swap">
<style>
  :root {
    --page-bg: #3e3e3e;
    --sky-top: #ffffff;
    --sky-mid: #d6effb;
    --sky-bottom: #8bd6f6;
    --navy: #14204a;
    --indigo: #263a7e;
    --brand-blue: #0677ba;
    --pill-text: #8fd8f7;
  }
  html, body {
    margin: 0;
    width: 1200px;
    height: 1200px;
    overflow: hidden;
    background: var(--page-bg);
  }
  .sign {
    position: absolute;
    left: 220px;
    top: 30px;
    width: 760px;
    height: 1140px;
    display: block;
  }
  .headline-light { font-family: 'Roboto', sans-serif; font-weight: 300; fill: var(--indigo); }
  .headline-bold { font-family: 'Roboto', sans-serif; font-weight: 900; fill: var(--navy); }
  .brand-name { font-family: 'Roboto', sans-serif; font-weight: 500; fill: var(--brand-blue); }
  .phone-number { font-family: 'Roboto', sans-serif; font-weight: 700; fill: var(--pill-text); }
</style>
</head>
<body>
<svg class="sign" viewBox="0 0 760 1140" xmlns="http://www.w3.org/2000/svg">
  <defs>
    <linearGradient id="sign-sky" x1="0" y1="0" x2="0" y2="1">
      <stop offset="0" stop-color="var(--sky-top)"/>
      <stop offset="0.45" stop-color="var(--sky-mid)"/>
      <stop offset="1" stop-color="var(--sky-bottom)"/>
    </linearGradient>
    <linearGradient id="base-band" x1="0" y1="0" x2="1" y2="0">
      <stop offset="0" stop-color="var(--indigo)"/>
      <stop offset="1" stop-color="var(--navy)"/>
    </linearGradient>
  </defs>

  <rect class="sign-face" x="0" y="0" width="760" height="1140" fill="url(#sign-sky)"/>

  <text class="headline-light" x="384" y="258" font-size="226" text-anchor="middle">FOR</text>
  <text class="headline-bold" x="380" y="450" font-size="226" text-anchor="middle">SALE</text>
  <rect class="headline-rule" x="256" y="474" width="250" height="4" rx="2" fill="var(--navy)"/>

  <g class="brand">
    <text class="brand-name" x="380" y="880" font-size="60" text-anchor="middle">Bluepine Ridge</text>
    <text class="brand-name" x="386" y="918" font-size="20" letter-spacing="24" text-anchor="middle">REALTY</text>
  </g>

  <g class="phone-pill">
    <rect x="78" y="949" width="608" height="88" rx="44" fill="var(--navy)"/>
    <g class="phone-icon" fill="none" stroke="var(--pill-text)" stroke-width="3.5" stroke-linecap="round" stroke-linejoin="round">
      <path d="M106 972 l9 -4 8 14 -6 6 q4 10 14 18 l6 -5 13 9 -4 9 q-6 5 -14 2 q-18 -8 -28 -30 q-3 -10 2 -19z"/>
      <path d="M130 976 q8 3 11 11"/>
      <path d="M132 967 q14 5 18 19"/>
      <path d="M134 958 q20 7 25 27"/>
    </g>
    <text class="phone-number" x="164" y="1019" font-size="74" textLength="496" lengthAdjust="spacingAndGlyphs">(555) 617 3489</text>
  </g>

  <rect class="base-band" x="0" y="1099" width="760" height="41" fill="url(#base-band)"/>
</svg>
</body>
</html>
```